International Travel Technology R&D business needs a wordpress website

We are a start up team of initially 2 individuals but plan to grow our team quickly, we have deep experience in travel technology. Our goal is to provide next generation technology research and development on behalf of our clients who are leading players in the travel technology industry. Attached our logos.

Target Market(s)

Travel Technology companies

Industry/Entity Type

Travel Industry

Coding

Coded - Design and coding required

Font styles to use
Sans Serif

Requirements
Must have
• Make use of our logo and colour scheme in the attached. Has to have a sense of adventure/ stepping into the unknown but equally must convey a sense of professionalism , we are a safe pair of hands. Sample themes are in the attachment .
Nice to have
• We have identified a theme on layoutbazaar which we feel would be inspirational. We hahe attached them to help in the design as inspiration.
Should not have
• images of airplanes , hotels etc, we want to project a future image.

```html
<!DOCTYPE html>
<html lang="en">
<head>
<meta charset="utf-8">
<title>Wayfront Labs</title>
<link href="https://fonts.googleapis.com/css2?family=Roboto:wght@400;500;700&family=Nothing+You+Could+Do&display=swap" rel="stylesheet">
<style>
:root{
  --sky:#4fb3f2;
  --sky-deep:#2f93e0;
  --sky-light:#7ccaf8;
  --green:#4cbb17;
  --ink:#222b33;
  --body:#4c5660;
  --pale:#f3f5f8;
  --white:#ffffff;
  --line:#6cc04a;
}
*{margin:0;padding:0;box-sizing:border-box}
html,body{width:1200px;height:2264px;overflow:hidden}
body{position:relative;font-family:"Roboto",Arial,sans-serif;color:var(--body);background:var(--white)}
.abs{position:absolute}

/* top bar */
.topbar{left:0;top:0;width:1200px;height:33px;background:var(--white)}
.topbar-item{top:8px;font-size:14px;color:var(--green);display:flex;align-items:center;gap:6px}
.login{top:6px;left:970px;height:22px;padding:0 8px;background:var(--green);color:var(--white);border-radius:4px;font-size:14px;font-weight:500;display:flex;align-items:center;gap:5px}
.dot-social{top:11px;width:11px;height:11px;border-radius:50%;background:var(--green)}

/* hero */
.hero{left:0;top:33px;width:1200px;height:559px;background:linear-gradient(120deg,#4f7fae 0%,#6d9cc6 40%,#3f6e9f 75%,#2f5d8e 100%)}
.navband{left:0;top:33px;width:1200px;height:68px;background:linear-gradient(90deg,rgba(79,179,242,.95),rgba(88,190,248,.95))}
.nav{top:58px;font-size:16px;font-weight:500;color:var(--white);text-transform:uppercase}
.logo-box{left:54px;top:0;width:281px;height:113px;background:var(--white);border-radius:0 0 10px 10px;box-shadow:0 2px 6px rgba(0,0,0,.15);display:flex;align-items:center;justify-content:center;gap:10px}
.logo-mark{width:18px;height:18px;border-radius:50%;background:var(--sky-deep)}
.logo-name{font-size:28px;font-weight:700;color:var(--sky-deep)}
.hero-title{left:0;top:160px;width:1200px;text-align:center;font-family:"Nothing You Could Do",cursive;font-size:74px;line-height:86px;color:var(--white)}
.hero-sub{left:0;top:346px;width:1200px;text-align:center;font-size:21px;line-height:31px;font-weight:500;color:var(--white)}
.btn{top:427px;height:33px;font-size:10px;font-weight:700;color:var(--white);display:flex;align-items:center;justify-content:center;text-transform:uppercase;border-radius:2px}
.btn-solid{left:494px;width:72px;background:var(--green)}
.btn-ghost{left:616px;width:95px;border:2px solid var(--green)}
.slider-dot{top:557px;width:10px;height:10px;border-radius:50%;border:2px solid var(--white)}
.slider-dot.on{background:var(--white)}

/* intro */
.intro{left:0;top:592px;width:1200px;height:359px;background:var(--pale)}
.section-title{left:0;width:1200px;text-align:center;font-size:22px;font-weight:700;color:var(--ink)}
.dotted{left:41px;width:1121px;border-top:2px dotted var(--line)}
.feature-icon{top:693px;width:76px;height:80px;border-radius:3px;background:linear-gradient(180deg,#6cc6fb,#3ea6ee);display:flex;align-items:center;justify-content:center}
.feature-title{top:782px;width:360px;text-align:center;font-size:19px;font-weight:500;color:var(--ink)}
.feature-text{top:824px;width:360px;text-align:center;font-size:12.5px;line-height:19.6px}

/* city band */
.city{left:0;top:951px;width:1200px;height:276px;background:linear-gradient(180deg,#4a79a8 0%,#3b5f86 45%,#2a3f5a 100%)}
.city-caption{left:4px;top:1193px;font-family:"Nothing You Could Do",cursive;font-size:19px;color:var(--white)}

/* services */
.illustration{left:53px;top:1336px;width:533px;height:405px;background:linear-gradient(180deg,#e4f3fe 0%,#bfe3fb 65%,#a9d9f8 100%)}
.acc-item{left:614px;display:flex;align-items:center;gap:12px;font-size:16.5px;color:var(--ink)}
.acc-icon{width:26px;height:26px;border-radius:3px;background:#eef2f6;display:flex;align-items:center;justify-content:center}
.acc-item.open{color:var(--sky-deep)}
.acc-item.open .acc-icon{background:var(--sky-deep)}
.acc-text{left:652px;top:1386px;width:500px;font-size:13px;line-height:19px}
.skyline{left:0;top:1751px;width:1200px;height:68px;background:linear-gradient(180deg,rgba(79,179,242,0) 0%,rgba(79,179,242,.35) 60%,rgba(79,179,242,.7) 100%)}

/* footer */
.footer{left:0;top:1819px;width:1200px;height:445px;background:linear-gradient(180deg,#4aa8ee 0%,#6cc3f8 55%,#55b4f2 100%);color:var(--white)}
.foot-head{top:1872px;font-size:19px;font-weight:500;color:var(--white)}
.foot-text{font-size:12.5px;line-height:19px;color:var(--white);width:254px}
.field{left:334px;width:252px;background:var(--white);border-radius:3px;font-size:12.5px;color:#8a949c;padding:8px 14px}
.send{left:334px;top:2091px;width:134px;height:32px;background:var(--green);color:var(--white);font-size:13px;font-weight:700;display:flex;align-items:center;justify-content:center;border-radius:2px}
.map{left:614px;top:1911px;width:254px;height:216px;background:linear-gradient(135deg,#e8eef0,#d6e4e8 60%,#b9d3dd)}
.foot-social{top:2095px;width:13px;height:13px;border-radius:50%;background:var(--white)}
.foot-rule{left:53px;top:2193px;width:1094px;border-top:1px solid rgba(255,255,255,.7)}
.copyright{left:0;top:2222px;width:1200px;text-align:center;font-size:12.5px;font-weight:500;color:var(--white)}
</style>
</head>
<body>

<!-- top bar -->
<div class="abs topbar"></div>
<div class="abs topbar-item" style="left:632px">
  <svg width="12" height="12" viewBox="0 0 24 24"><path fill="#4cbb17" d="M6.6 10.8a15 15 0 0 0 6.6 6.6l2.2-2.2c.3-.3.7-.4 1-.2 1.1.4 2.3.6 3.6.6.6 0 1 .4 1 1V20c0 .6-.4 1-1 1A17 17 0 0 1 3 4c0-.6.4-1 1-1h3.5c.6 0 1 .4 1 1 0 1.3.2 2.5.6 3.6.1.3 0 .7-.2 1z"/></svg>
  +1 800 555 01 24
</div>
<div class="abs topbar-item" style="left:784px">
  <svg width="13" height="11" viewBox="0 0 26 20"><rect width="26" height="20" rx="2" fill="#4cbb17"/><path d="M2 3l11 8 11-8" stroke="#fff" stroke-width="2" fill="none"/></svg>
  hello@wayfrontlabs.com
</div>
<div class="abs login">
  <svg width="11" height="11" viewBox="0 0 20 20"><path d="M2 10h11M9 6l4 4-4 4" stroke="#fff" stroke-width="2.4" fill="none"/><path d="M12 3h5v14h-5" stroke="#fff" stroke-width="2.4" fill="none"/></svg>
  Login
</div>
<div class="abs dot-social" style="left:1053px"></div>
<div class="abs dot-social" style="left:1091px"></div>
<svg class="abs" style="left:1132px;top:10px" width="13" height="13" viewBox="0 0 20 20"><circle cx="8" cy="8" r="6" stroke="#4cbb17" stroke-width="2.6" fill="none"/><path d="M12.5 12.5l5.5 5.5" stroke="#4cbb17" stroke-width="3"/></svg>

<!-- hero -->
<div class="abs hero" role="img" aria-label="Photo of two business people shaking hands over a desk with a tablet, in a blue tint"></div>
<div class="abs navband"></div>
<div class="abs logo-box"><span class="logo-mark"></span><span class="logo-name">Wayfront Labs</span></div>
<nav>
  <span class="abs nav" style="left:548px">Home</span>
  <span class="abs nav" style="left:634px">Company</span>
  <span class="abs nav" style="left:750px">Services</span>
  <span class="abs nav" style="left:866px">Solutions</span>
  <span class="abs nav" style="left:995px">Blog</span>
  <span class="abs nav" style="left:1075px">Contact</span>
</nav>
<h1 class="abs hero-title" style="font-weight:400">Welcome to<br>Wayfront Labs</h1>
<p class="abs hero-sub">Your trusted market research provider, dedicated to the<br>provision of meaningful and actionable insights</p>
<span class="abs btn btn-solid">About us</span>
<span class="abs btn btn-ghost">Go on surfing</span>
<span class="abs slider-dot on" style="left:566px"></span>
<span class="abs slider-dot" style="left:584px"></span>
<span class="abs slider-dot on" style="left:602px"></span>
<span class="abs slider-dot on" style="left:620px"></span>

<!-- intro -->
<section class="abs intro"></section>
<h2 class="abs section-title" style="top:613px">Partners &amp; Travel Technology Companies</h2>
<div class="abs dotted" style="top:653px"></div>

<div class="abs feature-icon" style="left:187px">
  <svg width="38" height="38" viewBox="0 0 40 40"><path d="M6 18h7v18H6zM15 35V19l7-12c2-2 5-1 5 2l-2 8h9c2 0 3 2 3 4l-3 11c-.5 2-2 3-4 3z" fill="none" stroke="#fff" stroke-width="2.4" stroke-linejoin="round"/></svg>
</div>
<div class="abs feature-icon" style="left:560px">
  <svg width="38" height="38" viewBox="0 0 40 40"><path d="M20 4c5 5 6 12 4 20h-8c-2-8-1-15 4-20z" fill="none" stroke="#fff" stroke-width="2.2"/><circle cx="20" cy="15" r="2.5" fill="none" stroke="#fff" stroke-width="2"/><path d="M16 22l-4 6 5-1M24 22l4 6-5-1M18 29l2 6 2-6" fill="none" stroke="#fff" stroke-width="2"/></svg>
</div>
<div class="abs feature-icon" style="left:936px">
  <svg width="34" height="38" viewBox="0 0 34 40"><path d="M5 3h17l8 8v26H5z" fill="none" stroke="#fff" stroke-width="2.4"/><path d="M22 3v8h8M10 18h14M10 24h14M10 30h14" stroke="#fff" stroke-width="2.2" fill="none"/></svg>
</div>

<h3 class="abs feature-title" style="left:45px">Who we are</h3>
<h3 class="abs feature-title" style="left:418px">Our Mission</h3>
<h3 class="abs feature-title" style="left:794px">Our Vision</h3>
<p class="abs feature-text" style="left:45px">The quality perception of the product, what clients would like to change, what price can they afford, where is this product wanted the most, what causes dissatisfaction in a product (i.e. price, quality,design)</p>
<p class="abs feature-text" style="left:418px">Wayfront Labs is a team of research professionals that work toward delivering research services while upholding the highest standards of design, analysis and reporting. Our mission is to help set the industry in consulting services</p>
<p class="abs feature-text" style="left:794px">Our vision is to be a long-term preferred partner to our clients in the field of market research and business consulting. We are relentlessly focused on delivering exceptional value in provision of strategy, research and analysis</p>

<!-- city band -->
<div class="abs city" role="img" aria-label="Aerial photo of a dense city skyline at dusk"></div>
<span class="abs city-caption">Parallax image move on mause scroll</span>

<!-- services -->
<h2 class="abs section-title" style="top:1252px">What We Do</h2>
<div class="abs dotted" style="top:1293px"></div>
<div class="abs illustration" role="img" aria-label="Flat blue illustration of three analysts working at laptops before a city backdrop with chart dashboards above"></div>

<div class="abs acc-item open" style="top:1352px">
  <span class="acc-icon"><svg width="12" height="8" viewBox="0 0 12 8"><path d="M1 7l5-5 5 5" stroke="#fff" stroke-width="2" fill="none"/></svg></span>
  Opinion Polling
</div>
<p class="abs acc-text">Opinion polls are an integral part of political debates, the state of the economy, social trends and more. Simply put, we report what people think, along with what they do, because it is important. We generate original public opinion data and other information that is relevant, timely and accurate</p>

<div class="abs acc-item" style="top:1488px"><span class="acc-icon"><svg width="10" height="7" viewBox="0 0 12 8"><path d="M1 1l5 5 5-5" stroke="#4fb3f2" stroke-width="2" fill="none"/></svg></span>Social and Economic Policy Analysis</div>
<div class="abs acc-item" style="top:1544px"><span class="acc-icon"><svg width="10" height="7" viewBox="0 0 12 8"><path d="M1 1l5 5 5-5" stroke="#4fb3f2" stroke-width="2" fill="none"/></svg></span>Project Evaluation and Impact Assessment</div>
<div class="abs acc-item" style="top:1601px"><span class="acc-icon"><svg width="10" height="7" viewBox="0 0 12 8"><path d="M1 1l5 5 5-5" stroke="#4fb3f2" stroke-width="2" fill="none"/></svg></span>Feasibility Studies</div>
<div class="abs acc-item" style="top:1657px"><span class="acc-icon"><svg width="10" height="7" viewBox="0 0 12 8"><path d="M1 1l5 5 5-5" stroke="#4fb3f2" stroke-width="2" fill="none"/></svg></span>New Product Development</div>
<div class="abs acc-item" style="top:1713px"><span class="acc-icon"><svg width="10" height="7" viewBox="0 0 12 8"><path d="M1 1l5 5 5-5" stroke="#4fb3f2" stroke-width="2" fill="none"/></svg></span>Market Size and Segmentation Studies</div>

<div class="abs skyline" role="img" aria-label="Blue silhouette strip of a city skyline and an airport"></div>

<!-- footer -->
<footer class="abs footer"></footer>
<h4 class="abs foot-head" style="left:53px">Contact Us</h4>
<h4 class="abs foot-head" style="left:334px">Feel Free to Mail</h4>
<h4 class="abs foot-head" style="left:614px">Headquarters</h4>
<h4 class="abs foot-head" style="left:895px">Last Review</h4>

<p class="abs foot-text" style="left:53px;top:1913px">Maecenas etos sit amet, consectetur adipiscing elit. Terminal volutpat rutrum metro amet sollicitudin interdum.</p>
<p class="abs foot-text" style="left:53px;top:1985px"><b>Phone:</b> +1 (800) 555 01 37</p>
<p class="abs foot-text" style="left:53px;top:2019px"><b>Office:</b> 418 Larkin Avenue, Port Wren</p>
<p class="abs foot-text" style="left:53px;top:2052px"><b>Email:</b> team@wayfrontlabs.com</p>
<span class="abs foot-social" style="left:53px"></span>
<span class="abs foot-social" style="left:76px"></span>
<span class="abs foot-social" style="left:102px"></span>
<span class="abs foot-social" style="left:133px"></span>
<span class="abs foot-social" style="left:161px"></span>

<div class="abs field" style="top:1913px;height:32px">Name *</div>
<div class="abs field" style="top:1964px;height:32px">Email *</div>
<div class="abs field" style="top:2015px;height:56px">Write Your Message Here...</div>
<span class="abs send">SEND MESSAGE</span>

<div class="abs map" role="img" aria-label="Street map of the headquarters area"></div>

<p class="abs foot-text" style="left:895px;top:1913px">Enim congue blandit. Lorem ipsum dolor sit amet, consectetur adipiscing elit. Quisque consectetur interdum finibus. Vestibulum ante ipsum primis in faucibus orci. luctus et ultrices posuere.</p>
<p class="abs foot-text" style="left:895px;top:2019px">Cubilia cras blandit finibus ipsum, id porttitor arcu volutpat a. Integer iaculis erat nec justo malesuada faucibus vel tempus sapien. Vivamus aliquam euismod tristique.</p>

<div class="abs foot-rule"></div>
<p class="abs copyright">Copyright 2020. All Rights Reserved by Wayfront Labs</p>

</body>
</html>
```